Plumwhirl Brochure - Tri Fold

Need to design a brochure for my business. Our colors are Pink/Black/White. I have included a new ad that I like the colors. This is a Cake Business that features gourmet cupcakes(retail and special order) , Custom Cakes for special occasions, Our retail shop which features our cupcakes, gelato, coffee, tea.

Focus should be on: Custom Cupcake orders for meetings, groups, schools, etc (catering).. Custom Cakes (special events - weddings, birthdays etc., Retail Sales (cupcakes, gelato, coffee, tea espresso at our Shop, Decorating Classes/birthday parties.

See our sample brochure and advertisements for colors and some content

Like to have a map on the back with our address, website, phone number

Target Market(s)

People ordering cupcakes for meetings, parties, events, school functions
Retail customers coming to our shop to enjoy our products
People ordering custom cakes for their special occasions
Cake Decorating classes/Birthday parties

Industry/Entity Type

Retail

Font styles to use
Serif
Sans Serif

Colors
ffffff
e567a6
1b1b1b
ebebeb

Requirements
Must have
• Custom Cupcake orders
Custom Cakes
Retail Customers

website
telephone numbers
facebook page
address
hours of operation
Nice to have
• The custom orders are the priority
followed by the retail
followed by cake decorating classes/birthday parties

```html
<!DOCTYPE html>
<html lang="en">
<head>
<meta charset="utf-8">
<title>Plumwhirl Cake House – Tri-Fold Brochure</title>
<link rel="stylesheet" href="https://fonts.googleapis.com/css2?family=Noto+Sans:wght@400;700&family=Titan+One&family=Indie+Flower&display=swap">
<style>
  :root {
    --pink: #e567a6;
    --pink-light: #ef8fbe;
    --pink-pale: #f8c9dd;
    --black: #1b1b1b;
    --white: #ffffff;
    --grey: #ebebeb;
    --cocoa: #3b1f14;
    --body-font: "Noto Sans", Verdana, sans-serif;
    --display-font: "Titan One", "Noto Sans", sans-serif;
    --script-font: "Indie Flower", cursive;
  }
  * { margin: 0; padding: 0; box-sizing: border-box; }
  html, body { width: 1200px; height: 848px; overflow: hidden; background: var(--white); }
  .brochure {
    position: relative; width: 1200px; height: 848px; overflow: hidden;
    font-family: var(--body-font); color: var(--white); font-size: 15px; line-height: 20px;
    background: var(--black);
  }
  .panel { position: absolute; top: 0; height: 848px; }
  .panel-left { left: 0; width: 402px; background: linear-gradient(150deg, var(--pink-light) 0%, var(--pink) 45%, var(--pink) 100%); }
  .panel-middle { left: 402px; width: 398px; background: var(--black); }
  .panel-right { left: 800px; width: 400px; background: linear-gradient(160deg, #ea7db3 0%, var(--pink) 100%); }

  .scallop { position: absolute; left: 0; top: 762px; }
  .footer-band { position: absolute; left: 0; top: 774px; width: 1200px; height: 74px; background: var(--black); }

  .abs { position: absolute; }

  .badge { position: absolute; }
  .badge svg { position: absolute; inset: 0; }
  .badge-title {
    position: absolute; inset: 0; display: flex; align-items: center; justify-content: center;
    font-family: var(--display-font); color: var(--cocoa); text-align: center; font-weight: 400;
  }

  .cupcakes-badge { left: 114px; top: 50px; width: 168px; height: 64px; }
  .cupcakes-badge .badge-title { font-size: 29px; }
  .intro { left: 60px; top: 128px; width: 318px; text-align: right; }

  .feature-list { left: 28px; top: 228px; list-style: none; }
  .feature-list li { position: relative; padding-left: 20px; height: 20px; white-space: nowrap; }
  .feature-list li::before {
    content: ""; position: absolute; left: 2px; top: 5px; width: 10px; height: 10px;
    border-radius: 50% 50% 30% 30%; background: var(--black);
  }
  .feature-list .indent::before { display: none; }
  .cupcake-photo {
    left: 262px; top: 214px; width: 80px; height: 74px; border-radius: 40%;
    background: radial-gradient(circle at 45% 45%, #d7f0ea 0%, #b9dfe0 40%, #f1b9d2 75%, rgba(229,103,166,0) 100%);
  }

  .rule { position: absolute; height: 2px; background: linear-gradient(90deg, rgba(255,255,255,0), var(--pink-pale), rgba(255,255,255,0)); }
  .rule-top { left: 130px; top: 389px; width: 120px; }
  .rule-bottom { left: 60px; top: 711px; width: 260px; }

  .gelato-badge { left: 250px; top: 356px; width: 132px; height: 60px; }
  .gelato-badge .badge-title { font-size: 27px; }
  .gelato-text { left: 22px; top: 424px; width: 370px; }

  .coffee-badge { left: 424px; top: 46px; width: 196px; height: 148px; }
  .coffee-badge .badge-title { font-size: 29px; line-height: 34px; }
  .coffee-text { left: 618px; top: 48px; width: 162px; text-align: right; }

  .cake-badge { left: 530px; top: 266px; width: 110px; height: 56px; }
  .cake-badge .badge-title { font-size: 27px; }
  .cake-intro { left: 402px; top: 338px; width: 398px; text-align: center; }

  .promise-band {
    position: absolute; left: 402px; top: 408px; width: 398px; height: 50px;
    background: linear-gradient(90deg, #e97cb2, var(--pink), #e97cb2);
    font-family: var(--script-font); color: var(--white); font-size: 15px; line-height: 18px;
    text-align: center; padding-top: 7px;
  }

  .design-heading { left: 402px; top: 470px; width: 398px; text-align: center; }
  .occasion-list { top: 494px; list-style: none; }
  .occasion-list li { position: relative; padding-left: 20px; height: 20px; white-space: nowrap; }
  .occasion-list li::before {
    content: ""; position: absolute; left: 2px; top: 5px; width: 10px; height: 10px;
    border-radius: 50% 50% 30% 30%; background: var(--white);
  }
  .occasion-list-a { left: 454px; }
  .occasion-list-b { left: 593px; }

  .cake-photo-baby { left: 462px; top: 568px; width: 104px; height: 200px; border-radius: 14px 14px 40px 40px;
    background: linear-gradient(180deg, #8fc8e0 0%, #f5f1f4 30%, #f4b6cf 60%, #9fcfe6 85%, #d9d9d9 100%); }
  .cake-photo-tiered { left: 604px; top: 566px; width: 146px; height: 200px; border-radius: 20px 20px 40px 40px;
    background: linear-gradient(180deg, #7fb36b 0%, #b6dcc9 35%, #8cc0a2 65%, #3f6b3a 100%); }

  .contact { left: 402px; top: 794px; width: 398px; text-align: center; line-height: 22px; }

  .shop-info { left: 22px; top: 790px; width: 370px; font-size: 13px; line-height: 18px; }
  .shop-info strong { color: var(--pink); font-weight: 700; }
  .social { left: 820px; top: 790px; width: 260px; font-size: 13px; line-height: 18px; }
  .social strong { color: var(--pink); font-weight: 700; }
  .map { left: 1090px; top: 784px; width: 96px; height: 56px; border-radius: 4px;
    background: linear-gradient(135deg, var(--grey) 0%, #d6d6d6 100%); }

  .classes-heading { left: 820px; top: 22px; color: var(--black); font-size: 15px; font-weight: 400; }
  .cupcake-hero {
    left: 888px; top: 264px; width: 312px; height: 506px;
    background: radial-gradient(ellipse at 75% 55%, #b07a5c 0%, #9b6546 35%, #8a5a40 55%, rgba(229,103,166,0) 80%);
  }
  .classes-text { left: 820px; top: 54px; width: 370px; white-space: nowrap; }
  .brand-mark { color: var(--black); font-weight: 700; }
</style>
</head>
<body>
<main class="brochure">

  <section class="panel panel-left" aria-label="Cupcakes and gelato"></section>
  <section class="panel panel-middle" aria-label="Coffee and custom cakes"></section>
  <section class="panel panel-right" aria-label="Cake decorating classes"></section>

  <svg class="scallop" width="1200" height="24" viewBox="0 0 1200 24" aria-hidden="true">
    <defs>
      <pattern id="scallop-dots" width="24" height="24" patternUnits="userSpaceOnUse">
        <circle cx="12" cy="14" r="10" fill="#1b1b1b"/>
      </pattern>
    </defs>
    <rect x="0" y="0" width="1200" height="24" fill="url(#scallop-dots)"/>
  </svg>
  <div class="footer-band"></div>

  <!-- Cupcakes -->
  <div class="badge cupcakes-badge">
    <svg viewBox="0 0 168 64" width="168" height="64" aria-hidden="true">
      <path d="M14 6 H154 Q164 6 162 16 Q156 32 162 48 Q164 58 154 58 H14 Q4 58 6 48 Q12 32 6 16 Q4 6 14 6 Z" fill="#f8c9dd" stroke="#fff" stroke-width="3"/>
    </svg>
    <h2 class="badge-title">Cupcakes</h2>
  </div>
  <p class="abs intro">We make all our cupcakes with a little<br>“bling” just to give them that sparkle<br>that makes not only delicious to eat,<br>but beautiful to see.</p>

  <ul class="abs feature-list">
    <li>Baked Fresh Daily</li>
    <li>Daily Specials Cupcakes</li>
    <li>Unique Flavors</li>
    <li>Catering for Parties and Events</li>
    <li>Special Orders for Business</li>
    <li class="indent">Meetings and Weddings</li>
  </ul>
  <div class="abs cupcake-photo" role="img" aria-label="Photo of pastel decorated cupcakes"></div>

  <div class="rule rule-top"></div>
  <div class="badge gelato-badge">
    <svg viewBox="0 0 132 60" width="132" height="60" aria-hidden="true">
      <path d="M12 6 H120 Q130 6 128 16 Q122 30 128 44 Q130 54 120 54 H12 Q2 54 4 44 Q10 30 4 16 Q2 6 12 6 Z" fill="#f8c9dd" stroke="#fff" stroke-width="3"/>
    </svg>
    <h2 class="badge-title">Gelato</h2>
  </div>
  <p class="abs gelato-text">Gelato is Italian Ice Cream made with<br>significantly less fat than traditional ice<br>cream.&nbsp; Our gelato and sorbetto is made<br>from scratch.&nbsp; Each batch of gelato and<br>sorbetto is made to order fresh with<br>authentic, Italian flavors and raw ingredients.<br>Natural ingredients and fresh fruits are used<br>in our Gelato and Sorbetto. Only the highest<br>quality creams, fruits, nuts, spices, liqueurs,<br>imported chocolates, coffees and teas are<br>used. We invite everyone in the area to<br>come in and try a few flavors to see what<br>your favorite is before ordering.</p>
  <div class="rule rule-bottom"></div>

  <!-- Coffee -->
  <div class="badge coffee-badge">
    <svg viewBox="0 0 196 148" width="196" height="148" aria-hidden="true">
      <path d="M16 6 H180 Q192 6 190 18 Q182 74 190 130 Q192 142 180 142 H16 Q4 142 6 130 Q14 74 6 18 Q4 6 16 6 Z" fill="#f8c9dd" stroke="#fff" stroke-width="3"/>
    </svg>
    <h2 class="badge-title">Espresso<br>Cappuchino<br>Coffee Tea</h2>
  </div>
  <p class="abs coffee-text">If you want a great<br>cup of coffee or tea,<br>you have to stop in<br>TPCH. We offer<br>imported Italian<br>Coffee and an<br>Assortment of freshly<br>brewed organic Tea.</p>

  <!-- Cake -->
  <div class="badge cake-badge">
    <svg viewBox="0 0 110 56" width="110" height="56" aria-hidden="true">
      <path d="M12 6 H98 Q108 6 106 16 Q100 28 106 40 Q108 50 98 50 H12 Q2 50 4 40 Q10 28 4 16 Q2 6 12 6 Z" fill="#f8c9dd" stroke="#fff" stroke-width="3"/>
    </svg>
    <h2 class="badge-title">Cake</h2>
  </div>
  <p class="abs cake-intro">Custom Cakes by our Amazing Decorator Marnie<br>We provide extraordinary cakes<br>for every special occasion</p>

  <p class="promise-band">All cakes are made fresh from scratch. We<br>collaborate with our clients to suite the occasion.</p>

  <p class="abs design-heading">We design cakes for:</p>
  <ul class="abs occasion-list occasion-list-a">
    <li>Weddings</li>
    <li>Birthdays</li>
    <li>Anniversaries</li>
  </ul>
  <ul class="abs occasion-list occasion-list-b">
    <li>Bridal Showers</li>
    <li>Baby Showers</li>
    <li>Special Occasions</li>
  </ul>

  <div class="abs cake-photo-baby" role="img" aria-label="Photo of a two-tier baby shower cake in pink, blue and white"></div>
  <div class="abs cake-photo-tiered" role="img" aria-label="Photo of a three-tier green themed birthday cake"></div>

  <!-- Footer -->
  <address class="abs shop-info" style="font-style:normal;">
    <strong>Visit us:</strong> 1280 Orchard Lane, Suite 4, Maple Grove<br>
    <strong>Hours:</strong> Tue–Sat 10am–7pm &nbsp;·&nbsp; Sun 12pm–5pm
  </address>
  <p class="abs contact">555-014-2277<br>www.theplumwhirlcakehouse.com</p>
  <p class="abs social"><strong>Find us on Facebook:</strong><br>facebook.com/theplumwhirlcakehouse</p>
  <div class="abs map" role="img" aria-label="Map showing the shop location on Orchard Lane"></div>

  <!-- Classes -->
  <div class="abs cupcake-hero" role="img" aria-label="Close-up photo of a chocolate frosted cupcake with sprinkles"></div>
  <h2 class="abs classes-heading">Cake Decorating Classes and Parties</h2>
  <p class="abs classes-text"><span class="brand-mark">TPCH</span> offers a variety of cake decorating<br>classes. Whether you are an amateur who<br>has never baked a cake, or a more advanced<br>cake decorator, there is something for you<br>in our selection of classes. In our classes<br>you will learn the best expert decorating<br>techniques for cakes, cookies, cupcakes and<br>cake pops. All our classes are “hands-on,” so<br>when the class is over you will have a<br>creation to take home to show and savor<br>with your loved ones. We will use the same<br>tools and methods as we do when making<br>our own cakes in our shop. Many of our<br>sessions will be taught by a master cake<br>decorator and culinary arts instructor.<br>Classes are conducted in small<br>groups, allowing for personal<br>attention to each student.<br>You should reserve your<br>place ahead of time to<br>ensure a space Please<br>call for more details<br>and the schedule.</p>

</main>
</body>
</html>
```